Label Design For My Pet Supplements Brand - Probiotic Dog Chews

Good Afternoon!
I am looking for a revamp of our current label design for my Probiotic Dog Chews. Attached is our current label and a mockup as well. I do like and appreciate our current design, but it lacks character, and appears to be really similar to other brands out there. I would like for the new label to take all the great characteristics of this label, but elevate them.
For context, our product is a 10oz White Jar with a White Lid.
I am attaching a full comprehensive guide that includes our existing files, fonts, .ai files, mockups, and our Brand Strategy. That way you're able to get an idea of what it is we sell and who exactly our customer is too. And that way we are able to create a label that speaks to our exact ideal customer. I am also supplying to you all the details for the label as well.
If you have any questions for me, feel free to ask. I'm looking forward to seeing your work!

```html
<!DOCTYPE html>
<html lang="en">
<head>
<meta charset="utf-8">
<title>Tailbright Probiotic Chews – Label</title>
<link href="https://fonts.googleapis.com/css2?family=Luckiest+Guy&family=Oswald:wght@400;500;600&family=Montserrat:wght@500;700&family=Roboto+Slab:wght@700&display=swap" rel="stylesheet">
<style>
  :root {
    --teal: #6cc1ab;
    --teal-deep: #5cae98;
    --teal-line: #9fd8c9;
    --white: #ffffff;
    --cream: #f4f8f5;
    --coral: #e8775d;
    --coral-deep: #d9644b;
    --rust: #a8634f;
    --chew: #c99a5a;
    --chew-dark: #9a6a35;
    --page: #ecebe7;
    --badge: #e9eef4;
  }
  * { box-sizing: border-box; margin: 0; padding: 0; }
  html, body { width: 790px; height: 1200px; overflow: hidden; }
  body {
    background: var(--page);
    font-family: "Oswald", sans-serif;
    color: var(--white);
    position: relative;
  }
  .label {
    position: absolute;
    left: 0; top: 520px;
    width: 790px; height: 159px;
    background: var(--teal);
    border-radius: 6px;
    overflow: hidden;
  }
  .label > * { position: absolute; }

  /* ingredients column */
  .ingredients { left: 16px; top: 22px; width: 144px; }
  .ingredients p {
    font-size: 4.6px; line-height: 1.55; text-transform: uppercase; letter-spacing: 0.02em;
  }
  .ingredients b { font-weight: 600; }
  .ingredients hr { border: 0; border-top: 0.6px solid var(--teal-line); margin: 6px 0; }
  .tag-no-lies {
    display: inline-block; background: var(--coral); color: var(--white);
    padding: 0 2px; border-radius: 1px; font-weight: 600;
  }

  /* centre panel */
  .panel-disc {
    left: 212px; top: -30px; width: 200px; height: 220px;
    border-radius: 50%; background: var(--teal-deep); opacity: 0.35;
  }
  .brand {
    left: 222px; top: 12px; width: 180px; text-align: center;
    font-family: "Oswald", sans-serif; font-weight: 600; font-size: 13px; letter-spacing: 0.01em;
  }
  .title {
    left: 238px; top: 40px; width: 150px;
    font-family: "Luckiest Guy", sans-serif; color: var(--white);
    text-align: center; line-height: 0.95;
  }
  .title .line1 { display: block; font-size: 27px; transform: rotate(4deg); }
  .title .line2 { display: block; font-size: 25px; margin-top: 2px; }
  .natural-badge {
    left: 226px; top: 112px; width: 34px; height: 30px;
    border-radius: 50%; background: var(--cream);
  }
  .chew-photo {
    left: 348px; top: 88px; width: 50px; height: 32px;
    border-radius: 10px; background: linear-gradient(135deg, var(--chew), var(--chew-dark));
  }
  .supplement {
    left: 360px; top: 122px; font-family: "Oswald", sans-serif; font-weight: 500;
    font-size: 5.4px; line-height: 1.15; text-transform: uppercase; text-align: right;
  }
  .supplement span { display: block; background: var(--cream); color: var(--rust); padding: 0 2px; border-radius: 1px; margin-bottom: 1px; }
  .flavor {
    left: 280px; top: 121px; font-family: "Roboto Slab", serif; font-size: 5px;
    transform: rotate(-10deg);
  }
  .count-pill {
    left: 284px; top: 129px; width: 52px; height: 24px; border-radius: 12px;
    background: var(--coral); text-align: center; padding-top: 4px;
    font-family: "Montserrat", sans-serif;
  }
  .count-pill strong { display: block; font-size: 8px; font-weight: 500; }
  .count-pill small { display: block; font-size: 2.8px; font-weight: 500; }

  /* how to use */
  .howto { left: 473px; top: 20px; width: 140px; }
  .howto h2, .benefits h2 {
    font-family: "Oswald", sans-serif; font-weight: 500; font-size: 7px; text-transform: uppercase; letter-spacing: 0.01em;
  }
  .step { display: flex; gap: 6px; margin-top: 6px; align-items: flex-start; }
  .step svg { flex: 0 0 14px; }
  .step h3 { font-size: 5px; font-weight: 600; text-transform: uppercase; }
  .step p { font-size: 4.4px; margin-top: 1px; }
  .howto hr { border: 0; border-top: 0.6px solid var(--teal-line); margin-top: 8px; }
  .benefits { left: 473px; top: 112px; width: 140px; }
  .benefits ul { list-style: none; display: grid; grid-template-columns: 1fr 1fr; gap: 3px 6px; margin-top: 6px; }
  .benefits li { font-size: 4.3px; display: flex; align-items: center; gap: 3px; }

  /* serving table */
  .serving {
    left: 629px; top: 12px; width: 117px; height: 94px;
    border: 0.8px solid var(--cream); border-radius: 2px;
  }
  .serving h2 {
    background: var(--cream); color: var(--teal-deep); font-family: "Montserrat", sans-serif;
    font-weight: 700; font-size: 6.5px; letter-spacing: 0.12em; padding: 3px 6px;
  }
  .serving table { width: 100%; border-collapse: collapse; font-size: 4.8px; }
  .serving th { font-weight: 400; font-size: 6px; text-align: left; padding: 3px 6px; border-bottom: 0.6px solid var(--cream); }
  .serving th + th, .serving td + td { border-left: 0.6px solid var(--cream); }
  .serving td { padding: 1px 6px; }
  .serving tr:nth-child(2) td { padding-top: 5px; }
  .company { left: 630px; top: 112px; font-size: 3.2px; line-height: 1.45; text-transform: uppercase; }

  /* certification badges */
  .badge { left: 756px; width: 28px; height: 28px; border-radius: 50%; background: var(--badge); }
  .badge.b1 { top: 12px; }
  .badge.b2 { top: 48px; background: #f2a27a; }
  .badge.b3 { top: 84px; }
  .badge.b4 { top: 120px; }
</style>
</head>
<body>
<section class="label" aria-label="Probiotic chews jar label">

  <div class="ingredients">
    <p><b>Base ingredients:</b> oat flour, sunflower oil, deionized water, flaxseed meal, vegetable glycerin, sunflower lecithin, guar gum, potassium sorbate, brewers yeast, organic vegetable blend (carrots, beets, apples, celery, lemon, cucumbers), vegan bacon flavor</p>
    <hr>
    <p><b>Actives:</b> P6 (6 probiotics @30B/CFU per package) prebiotic inulin, L.plantarum 5B/CFU, L.acidophilus 5B/CFU, L.casei 5B/CFU, B.bifidum 5B/CFU, L.lactis 5B/CFU, L.fermentum 5B/CFU, enzyme blend (lipase, cellulase, amylase, protease), pumpkin seed meal 100mg</p>
    <hr>
    <p>Non-GMO, no chemicals, no artificials, no fillers, no cellulose, no potato, no corn, no beans, <span class="tag-no-lies">No lies</span></p>
  </div>

  <div class="panel-disc"></div>
  <div class="brand">Tailbright</div>
  <h1 class="title"><span class="line1">Probiotic</span><span class="line2">Chews</span></h1>
  <div class="natural-badge" role="img" aria-label="100% natural and organic seal"></div>
  <div class="chew-photo" role="img" aria-label="Photo of two peanut butter probiotic chews"></div>
  <div class="flavor">Peanut Butter Flavor</div>
  <div class="count-pill"><strong>140 CT.</strong><small>NET CONTENTS 10 OZ.</small></div>
  <div class="supplement"><span>Supplement</span><span>For dogs</span></div>

  <div class="howto">
    <h2>How to use Tailbright Probiotic Chews</h2>
    <div class="step">
      <svg width="14" height="12" viewBox="0 0 14 12" fill="none" stroke="#fff" stroke-width="0.9"><path d="M2 2 L4 8 Q7 11 10 8 L12 2 Q9 4 7 4 Q5 4 2 2Z"/></svg>
      <div><h3>Hand feed</h3><p>Give the chew directly to your dog as a treat.</p></div>
    </div>
    <div class="step">
      <svg width="14" height="12" viewBox="0 0 14 12" fill="none" stroke="#fff" stroke-width="0.9"><ellipse cx="7" cy="5" rx="6" ry="2.5"/><path d="M1 5 Q2 10 7 10 Q12 10 13 5"/></svg>
      <div><h3>Crumble over food</h3><p>Crumble the chew over your dog's regular meal.</p></div>
    </div>
    <hr>
  </div>

  <div class="benefits">
    <h2>Product benefits ♥</h2>
    <ul>
      <li><svg width="5" height="4" viewBox="0 0 5 4"><path d="M0.5 2 L2 3.5 L4.5 0.5" stroke="#fff" stroke-width="0.6" fill="none"/></svg>Digestive Health</li>
      <li><svg width="5" height="4" viewBox="0 0 5 4"><path d="M0.5 2 L2 3.5 L4.5 0.5" stroke="#fff" stroke-width="0.6" fill="none"/></svg>Healthy Yeast Production</li>
      <li><svg width="5" height="4" viewBox="0 0 5 4"><path d="M0.5 2 L2 3.5 L4.5 0.5" stroke="#fff" stroke-width="0.6" fill="none"/></svg>Seasonal Allergies</li>
      <li><svg width="5" height="4" viewBox="0 0 5 4"><path d="M0.5 2 L2 3.5 L4.5 0.5" stroke="#fff" stroke-width="0.6" fill="none"/></svg>Scratching &amp; Paw Licking</li>
    </ul>
  </div>

  <div class="serving">
    <h2>SERVING SIZE</h2>
    <table>
      <tr><th>Body weight</th><th>Chews per day</th></tr>
      <tr><td>UNDER 10 LBS</td><td>1</td></tr>
      <tr><td>10-30 LBS</td><td>2</td></tr>
      <tr><td>31-60 LBS</td><td>3</td></tr>
      <tr><td>61-90 LBS</td><td>4</td></tr>
      <tr><td>OVER 90 LBS</td><td>5</td></tr>
    </table>
  </div>
  <div class="company">
    Tailbright, LLC<br>1200 Meadow Lane, Unit 5<br>Springfield, ST 00000<br>tailbright.example<br><br>Batch code: TB-0524<br>Best by: 01/2026
  </div>

  <div class="badge b1"></div>
  <div class="badge b2"></div>
  <div class="badge b3"></div>
  <div class="badge b4"></div>
</section>
</body>
</html>
```